Inspirational quotes poster shop seeks poster designs

Hi! We are launching an eshop with design posterss featuring inspirational quotes. We need a first poster design while looking for further cooperation on around 20 poster designs. We need outputs in the format that can go to high quality print (size at least 100x70cm).

For the first design feel free to choose any of the following quotes to depict:

1. "Stop starting. Start finishing." Author: Tobias Wrennholt, Plinkora
2. "A problem well stated is a problem half solved." Author: Walter J. Brimsley, American inventor
3. "The best way to predict the future is to invent it." Author: Frank Dolan, Quince

Designs should be rarther simple, think please of your whole concept and how various posters would go together. Every poster can be quite different though, in terms of fonts, colours and overall design, together they should however form and interesting collage.

Designs must contain the quote, author & company. it can be pure text or some indication of the sense of the quote.

Design must also feature company name/logo (not available yet, for now please use "brainvolter" as a working name), QR code with a title "Read the story"

See these posters for design we like (for inspiration ONLY!):
http://www.foundertonics.example/products/founder-print-its-simple-until-you-make-it-complicated
http://www.foundertonics.example/products/founder-print-marcus-pellway-less-meetings-more-doing
http://www.foundertonics.example/products/founder-print-lionel-habberg-stop-sketching-start-building
Updates

Hi to everybody! Sorry for the spam, some of you have been struggling with finding the crux in the quote, so here I offer some ideas what to look for in them. It's up to you to take it, leave it or change it:)

Stop starting, start finishing -
1 - stop starting with many times repeated small word starting, perhaps large word starting made of small words starting, with it contrasting start finishing in normal bold font.
2 - STARTING could look quite unfinished, sketchy, especially -ING could look more unfinished then the rest , e.g. just rough indication of outline of the letters, again contrasting with start finishing will clean & neat writting.

Problem well stated is a problem half solved - look for something that is clearer by defining the problem. Perhaps in a simple sketch like here http://www.foundertonics.example/products/founder-print-its-simple-until-you-make-it-complicated  point out a route from a problem (light = flame), to a solution (lightbulb, lightbulb design drawing or something like that).

Anyway, despite preference for simple design, I am still looking for some smart, creative, catchy idea in the design. Check with yourself if it's something you can would want to buy and hang up on your wall.

Good luck to all of you and again, thank you all very much for participation!
Radim

Target Market(s)

businesses of every size, from startups to large corporates seeking culture change or motivation kick up

Industry/Entity Type

Shop

Requirements
Must have
• I strongly prefer portrait orientation of the poster!

Nice to have
• Quotes themselves are often on the edge, teasing, so the design can be.
Should not have
• Try to avoid traditional dialoge bubble for the quote itself as the first obvious idea for depicting a quote.

Avoid using photos (not simple then) or too many colours.

Of course, by no means use a COPY of existing designs I linked to for inspiration. It just shows what we like.

```html
<!DOCTYPE html>
<html lang="en">
<head>
<meta charset="utf-8">
<title>Stop Starting Start Finishing — Poster</title>
<link rel="stylesheet" href="https://fonts.googleapis.com/css2?family=Anton&family=Open+Sans:wght@300;700&family=Playfair+Display:wght@900&display=swap">
<style>
  :root {
    --backdrop: #d8d8d8;
    --poster: #3a3a3c;
    --white: #ffffff;
    --yellow: #fdc80b;
    --quote-grey: #8c8c8e;
    --ink: #2b2b2b;
  }
  html, body {
    margin: 0;
    padding: 0;
    width: 1200px;
    height: 1000px;
    overflow: hidden;
    background: var(--backdrop);
  }
  .poster-canvas {
    display: block;
    width: 1200px;
    height: 1000px;
  }
  .poster-sheet { fill: var(--poster); }
  .brand-tag { fill: var(--white); }
  .brand-name {
    font-family: 'Open Sans', sans-serif;
    font-weight: 700;
    font-size: 12px;
    fill: var(--ink);
  }
  .brand-dot { fill: var(--ink); }
  .quote-mark {
    font-family: 'Playfair Display', serif;
    font-weight: 900;
    font-size: 165px;
    fill: var(--quote-grey);
  }
  .headline {
    font-family: 'Anton', sans-serif;
    font-size: 80px;
  }
  .headline--stop { fill: var(--white); }
  .headline--go { fill: var(--yellow); }
  .attribution {
    font-family: 'Open Sans', sans-serif;
    font-weight: 300;
    font-size: 22px;
    fill: var(--white);
  }
  .band-art { fill: var(--yellow); }
</style>
</head>
<body>
<svg class="poster-canvas" viewBox="0 0 1200 1000" xmlns="http://www.w3.org/2000/svg">
  <title>Stop starting, start finishing — Tobias Wrennholt, Plinkora</title>
  <defs>
    <filter id="sheet-shadow" x="-5%" y="-5%" width="110%" height="110%">
      <feDropShadow dx="3" dy="4" stdDeviation="4" flood-color="#000" flood-opacity="0.25"/>
    </filter>
  </defs>

  <rect class="poster-sheet" x="310" y="90" width="586" height="820" filter="url(#sheet-shadow)"/>

  <g class="brand">
    <polygon class="brand-tag" points="772,90 823,90 823,255 772,232"/>
    <text class="brand-name" transform="translate(802 208) rotate(-90)">brainvolter</text>
    <circle class="brand-dot" cx="797" cy="218" r="4"/>
  </g>

  <g class="quote">
    <text class="quote-mark" x="490" y="385">“</text>
    <text class="headline headline--stop" x="578" y="350" textLength="175" lengthAdjust="spacingAndGlyphs">STOP</text>
    <text class="headline headline--stop" x="422" y="438" textLength="331" lengthAdjust="spacingAndGlyphs">STARTING</text>
    <text class="headline headline--go" x="420" y="530" textLength="203" lengthAdjust="spacingAndGlyphs">START</text>
    <text class="headline headline--go" x="420" y="618" textLength="329" lengthAdjust="spacingAndGlyphs">FINISHING</text>
    <text class="quote-mark" x="756" y="700">”</text>
    <text class="attribution" x="425" y="658" textLength="323" lengthAdjust="spacing">Tobias Wrennholt, Plinkora</text>
  </g>

  <rect class="band-art" x="310" y="731" width="586" height="97" role="img" aria-label="Yellow band torn apart in the middle, illustrating unfinished work"/>
</svg>
</body>
</html>
```